Word document template for sales proposals

I am after a template that is simple but impactful. Use of colour to be limited but some for impact would be good. The proposals are for use in the professional technical field.

```html
<!DOCTYPE html>
<html lang="en">
<head>
<meta charset="utf-8">
<title>Proposal Template – Page Overview</title>
<link rel="stylesheet" href="https://fonts.googleapis.com/css2?family=Open+Sans:wght@400;600;700;800&family=Archivo:wght@700&display=swap">
<style>
:root{
  --navy:#1d3d6b;
  --blue:#3b7fc4;
  --band-blue:#4a8fd4;
  --orange:#ee7d2f;
  --ink:#3a3a3a;
  --paper:#ffffff;
  --bg:#ffffff;
}
*{box-sizing:border-box;margin:0;padding:0}
html,body{width:1037px;height:1200px;overflow:hidden;background:var(--bg)}
body{font-family:"Open Sans",Arial,sans-serif;color:var(--ink);position:relative}
.page{position:absolute;width:312px;height:222px;background:var(--paper);box-shadow:0 1px 5px rgba(0,0,0,.28);overflow:hidden}
.band{position:absolute;top:0;right:0;width:44px;height:100%;background:var(--orange)}
.brand{position:absolute;left:8px;bottom:8px;display:flex;align-items:center;gap:3px;font-weight:700;font-size:9px;color:var(--orange);letter-spacing:.5px}
.brand i{display:block;width:8px;height:8px;border-radius:50%;background:var(--blue)}
.title{position:absolute;font-weight:700;color:var(--blue);font-size:11px;text-transform:uppercase;line-height:1.15}
.sub{position:absolute;font-weight:600;color:#444;font-size:10px}
.body{position:absolute;font-size:5.2px;line-height:1.55;color:var(--ink)}
.body ul{list-style:none}
.body li{position:relative;padding-left:6px}
.body li::before{content:"";position:absolute;left:0;top:2.6px;width:2.2px;height:2.2px;border-radius:50%;background:var(--orange)}
.body p{margin-bottom:2px}
.photo{position:absolute}
.caption{position:absolute;left:0;width:100%;top:1104px;text-align:center;font-family:"Archivo",Arial,sans-serif;font-weight:700;font-size:16px;letter-spacing:3px;color:#111}
</style>
</head>
<body>

<!-- Row 1 -->
<section class="page" style="left:2px;top:31px">
  <div class="brand" style="top:10px;bottom:auto"><i></i>KELTRA</div>
  <div style="position:absolute;left:0;width:158px;top:52px;text-align:center">
    <div style="font-weight:800;font-size:23px;color:var(--navy)">PROPOSAL</div>
    <div style="font-size:6px;color:var(--blue)">Project name</div>
    <div style="font-size:5.5px;color:var(--blue);margin-top:42px">Prepared for</div>
    <div style="font-size:5.5px;font-weight:700;color:var(--navy);margin-top:6px">Brightmill Co</div>
    <div style="font-size:5.5px;color:var(--blue);margin-top:20px">Prepared by</div>
    <div style="font-size:5px;font-weight:700;color:var(--navy);margin-top:3px">Rowan Hale</div>
    <div style="font-size:4.6px;color:var(--navy)">rowan@kestrelworks.com</div>
  </div>
  <div class="photo" role="img" aria-label="Close-up photo of a water droplet on a green leaf" style="left:160px;top:0;width:152px;height:222px;background:radial-gradient(circle at 60% 40%,#9cc86a,#4b7d2c 55%,#1f3d14)"></div>
  <div style="position:absolute;left:200px;top:166px;color:#fff;font-weight:700;font-size:8px">October 19, 2023</div>
</section>

<section class="page" style="left:342px;top:31px">
  <div class="photo" role="img" aria-label="Photo of a business professional in an office with large windows" style="inset:0;background:linear-gradient(100deg,#6c7a83 0%,#9aa6ad 40%,#c3cbd0 70%,#aab3b8 100%)"></div>
  <div style="position:absolute;left:140px;top:20px;color:#fff;font-weight:700;font-size:14px">About us</div>
  <div class="body" style="left:140px;top:42px;width:160px;color:#fff;font-size:5.6px;line-height:1.6">
    <p>[Sender.Company] is a dynamic and innovative entity with a strong [Relevant Industry] track record. Founded on principles of excellence, creativity, and unwavering commitment to technological advancement, we have consistently demonstrated our ability to conceive, develop, and bring groundbreaking innovations that reshape industries to fruition. Our legal standing is firmly established, and we operate in full compliance with all applicable laws and regulations. [Sender.Company] holds itself to the highest ethical conduct and legal responsibility standards, ensuring that all our endeavours are conducted with utmost integrity and accountability.</p>
  </div>
  <div class="brand"><i></i>KELTRA</div>
</section>

<section class="page" style="left:683px;top:31px">
  <div style="position:absolute;left:0;top:0;width:100%;height:46px;background:var(--band-blue);color:#fff;font-weight:700;font-size:13px;text-align:center;line-height:36px">Project Overview</div>
  <div style="position:absolute;left:14px;top:52px;font-size:6.5px;font-weight:700;color:var(--blue)">Description</div>
  <div class="body" style="left:14px;top:64px;width:150px">
    <p>The product ("Name of Product") referenced in this proposal is a [Detailed Description of the Product]. It is designed, developed, and intended for use in accordance with all applicable laws and regulations. The Product is the proprietary creation of [Sender.Company] and is subject to all relevant intellectual property rights, including but not limited to patents, copyrights, and trademarks.</p>
  </div>
  <div style="position:absolute;left:206px;top:52px;font-size:6.5px;font-weight:700;color:var(--blue)">Technical specifications</div>
  <div class="body" style="left:206px;top:64px;width:96px">
    <p>The Product boasts the following technical specifications:</p>
    <ul style="margin-top:4px"><li>[List Key Technical Features and Specifications]</li><li>[Include Details of Any Prototypes or Demonstrations]</li></ul>
  </div>
  <div class="brand" style="left:auto;right:10px"><i></i>KELTRA</div>
</section>

<!-- Row 2 -->
<section class="page" style="left:2px;top:282px">
  <div class="band"></div>
  <div class="title" style="left:40px;top:13px">Scope of Work</div>
  <div class="sub" style="left:46px;top:36px">Inclusions</div>
  <div class="body" style="left:46px;top:56px;width:210px">
    <ul>
      <li>Requirement Analysis and Specification</li>
      <li>Analyze [Client.Company]'s needs and define technical specifications.</li>
      <li>System Design and Architecture</li>
      <li>Design a scalable, secure system with database structure and integrations.</li>
      <li>Software Development</li>
      <li>Develop [Specific Software/Product] to meet technical specifications.</li>
      <li>Testing and Quality Assurance</li>
      <li>Conduct thorough testing for performance and reliability.</li>
      <li>Deployment and Implementation</li>
      <li>Deploy [Specific Software/Product] and provide training.</li>
      <li>Post-Implementation Support</li>
      <li>Offer ongoing support, including bug fixes and updates.</li>
    </ul>
  </div>
  <div class="brand"><i></i>KELTRA</div>
</section>

<section class="page" style="left:342px;top:282px">
  <div class="band"></div>
  <div class="sub" style="left:48px;top:38px">Exclusions</div>
  <div class="body" style="left:50px;top:56px;width:210px">
    <ul>
      <li>Hardware Procurement: [Client.Company] responsible for hardware.</li>
      <li>Third-Party Licensing: Fees for third-party tools not included.</li>
      <li>Data Migration: Migration from legacy systems not covered.</li>
      <li>Customization Beyond Scope: Additional features may require separate agreement.</li>
    </ul>
  </div>
  <div class="brand"><i></i>KELTRA</div>
</section>

<section class="page" style="left:690px;top:287px">
  <div class="band"></div>
  <div class="title" style="left:36px;top:16px">Technical Approach</div>
  <div class="body" style="left:44px;top:40px;width:210px">
    <p>Our approach ensures a robust solution for [Client.Company]:</p>
    <ul style="margin:4px 0 4px 8px">
      <li>Requirement Refinement: Clarify project needs through detailed discussions.</li>
      <li>Agile Development: Embrace adaptability, transparency, and collaboration.</li>
      <li>Modular Architecture: Enhance scalability and facilitate future updates.</li>
      <li>Security and Compliance: Prioritize data protection and regulatory adherence.</li>
      <li>CI/CD Automation: Streamline testing, integration, and deployment.</li>
      <li>Scalability and Performance: Design for growth and optimize user experience.</li>
      <li>Quality Assurance: Rigorous testing for a high-quality final product.</li>
    </ul>
    <p>Our approach combines expertise and proven methodologies to align seamlessly with [Client.Company]'s objectives.</p>
  </div>
  <div class="brand"><i></i>KELTRA</div>
</section>

<!-- Row 3 -->
<section class="page" style="left:2px;top:532px">
  <div class="band"></div>
  <div class="title" style="left:40px;top:15px">Budget and Pricing</div>
  <div class="sub" style="left:50px;top:35px">Cost Breakdown</div>
  <div class="body" style="left:46px;top:56px;width:215px">
    <p>Development and Implementation: [Amount]</p>
    <ul>
      <li>This includes all expenses associated with software development, system deployment, and initial implementation.</li>
      <li>Testing and Quality Assurance: [Amount]</li>
      <li>Covers the cost of thorough testing procedures to ensure a high-quality final product.</li>
      <li>Post-Implementation Support: [Amount]</li>
      <li>Budget allocated for ongoing support, bug fixes, and updates following deployment.</li>
      <li>Hardware Procurement (Excluded): [Client's Responsibility]</li>
      <li>[Client.Company] will be responsible for procuring any necessary hardware infrastructure.</li>
      <li>Third-Party Licensing (Excluded): [Client's Responsibility]</li>
      <li>Licensing fees for third-party software or tools are not included in this proposal.</li>
    </ul>
  </div>
  <div class="brand"><i></i>KELTRA</div>
</section>

<section class="page" style="left:342px;top:532px">
  <div class="band"></div>
  <div class="sub" style="left:56px;top:28px">Payment schedule</div>
  <div class="body" style="left:62px;top:46px;width:200px">
    <p>The proposed payment schedule is as follows:</p>
  </div>
  <div class="brand"><i></i>KELTRA</div>
</section>

<section class="page" style="left:697px;top:529px">
  <div class="band"></div>
  <div class="title" style="left:28px;top:10px">Terms and Conditions</div>
  <div class="body" style="left:50px;top:30px;width:210px">
    <ul>
      <li>All payments are due within [Number of Days] days of invoice receipt.</li>
      <li>Late payments may incur a [Late Fee Percentage]% late fee.</li>
      <li>Invoices will be provided upon completion of each milestone.</li>
    </ul>
  </div>
  <div class="title" style="left:28px;top:76px">Exclusions</div>
  <div class="body" style="left:50px;top:96px;width:210px">
    <ul>
      <li>Hardware procurement and associated costs are excluded from this proposal.</li>
      <li style="margin-top:3px">Third-party licensing fees are not included.</li>
    </ul>
  </div>
  <div class="title" style="left:28px;top:150px">Contingency</div>
  <div class="body" style="left:50px;top:168px;width:215px">
    <p>A contingency budget of [Contingency Amount] is allocated to address unforeseen circumstances or scope adjustments during the project.</p>
  </div>
  <div class="brand"><i></i>KELTRA</div>
</section>

<!-- Row 4 -->
<section class="page" style="left:2px;top:785px;height:226px">
  <div class="band"></div>
  <div class="title" style="left:26px;top:11px">Intellectual Property<br>and Project Ownership</div>
  <div class="body" style="left:26px;top:42px;width:238px;font-size:5px">
    <p>In accordance with this legal provision of [Name of Jurisdiction] on Intellectual Property and Project Ownership, it is established that [Outline Ownership Rights of Each Party For Existing Intellectual Property].</p>
    <p>Notably, any newly generated intellectual property during the project, herein termed Project IP, shall be [Outline Ownership Rights of Each Party For New Intellectual Property].</p>
    <p>The agreement grants each party [Outline Usage Terms and Conditions For Trademarks, Patents or Copyrights]. Subsequent commercialization purposes shall be subject to [Outline Commercialization Procedures of The Intellectual Property].</p>
    <p>Additionally, robust measures for the protection of Project IP confidentiality are mandated, including cooperative efforts in patent applications, confidentiality obligations, and provisions for dispute resolution through mediation and arbitration, with governing law and jurisdiction set forth to govern legal actions arising from this agreement.</p>
    <p>All project-related materials, data, documents, prototypes, and other tangible items ("Project Materials") shall be jointly owned by [State The Ownership Status]. Each party shall have the right to retain copies of the project materials for its records.</p>
    <p>The parties agree to use the project materials solely for the purpose of fulfilling the project objectives and any subsequent commercialization efforts. Unauthorized use or disclosure of project materials is strictly prohibited.</p>
  </div>
  <div class="brand"><i></i>KELTRA</div>
</section>

<section class="page" style="left:342px;top:785px;height:226px">
  <div class="photo" role="img" aria-label="Landscape photo of green mountains and valley under a cloudy sky" style="inset:0;background:linear-gradient(180deg,#b8c8cf 0%,#7f9b8a 35%,#4f7a3a 60%,#3c6a2c 100%)"></div>
  <div style="position:absolute;left:0;width:100%;top:94px;text-align:center;color:#fff;font-weight:700;font-size:10.5px;line-height:1.35">We look forward to our cooperation<br>and are going to do eerything to<br>make it one GREAT success</div>
  <div style="position:absolute;left:0;width:100%;top:176px;display:flex;justify-content:center;align-items:center;gap:5px;font-weight:700;font-size:20px;color:var(--orange);letter-spacing:1px">
    <span style="display:block;width:18px;height:18px;border-radius:50%;background:var(--blue)"></span>KELTRA
  </div>
</section>

<div class="caption">Proposal done in word 11 pages</div>

</body>
</html>
```